Attorney business card for two offices

Looking for a new business card design that can list both of my offices, one in Houston and one in West Texas. Want something masculine, easy to read, and conservative yet somewhat modern. Our current card has used a nautical star on it for years, but I am not necessarily attached to that. Also, a lot of our forms use dark green and orange. Second office address is P.O. Box 518, Marathon, Texas 79617

```html
<!DOCTYPE html>
<html lang="en">
<head>
<meta charset="utf-8">
<title>Harlan Law Firm – Business Card</title>
<link href="https://fonts.googleapis.com/css2?family=Montserrat:wght@500;600;700&family=Cormorant+Garamond:wght@500&family=Lato:wght@500&display=swap" rel="stylesheet">
<style>
  :root {
    --green: #187a00;
    --brown: #8b5413;
    --ink: #111111;
    --paper: #ffffff;
    --silver: #cfcfcf;
    --page: #ffffff;
  }
  * { margin: 0; padding: 0; box-sizing: border-box; }
  html, body { width: 1200px; height: 1000px; overflow: hidden; background: var(--page); }
  .canvas { position: relative; width: 1200px; height: 1000px; }

  .card {
    position: absolute;
    left: 223px;
    width: 756px;
    height: 432px;
    box-shadow: 2px 3px 6px rgba(0,0,0,0.28);
    overflow: hidden;
  }
  .card-front { top: 42px; background: var(--paper); }
  .card-back { top: 526px; background: var(--green); }

  .t { position: absolute; white-space: nowrap; line-height: 1; }

  .attorney-name {
    left: 0; width: 100%; text-align: center; top: 80px;
    font: 600 41px "Montserrat", sans-serif; letter-spacing: 1px; color: var(--green);
  }
  .attorney-title {
    left: 0; width: 100%; text-align: center; top: 134px;
    font: 600 22px "Montserrat", sans-serif; letter-spacing: 1.5px; color: var(--brown);
  }
  .contact { font: 500 19px "Montserrat", sans-serif; color: var(--ink); line-height: 25px; }
  .phone { left: 63px; top: 224px; }
  .fax { left: 63px; top: 258px; }
  .office-houston { left: 63px; top: 305px; }
  .email { left: 440px; top: 258px; }
  .office-marathon { left: 440px; top: 305px; }

  .brand-mark { position: absolute; display: flex; align-items: center; gap: 6px; }
  .brand-mark .square { width: 18px; height: 18px; }
  .front-mark { left: 344px; top: 400px; }
  .front-mark .square { background: var(--brown); }
  .front-mark .name { font: 600 12px "Montserrat", sans-serif; letter-spacing: 1px; color: var(--brown); }

  .firm-name {
    left: 0; width: 100%; text-align: center; top: 176px;
    font: 500 40px "Cormorant Garamond", serif; letter-spacing: 1.5px; color: var(--silver);
  }
  .firm-tagline {
    left: 0; width: 100%; text-align: center; top: 234px;
    font: 500 19px "Lato", sans-serif; letter-spacing: 5px; color: var(--silver);
  }
  .rule { position: absolute; top: 245px; height: 1.5px; width: 55px; background: var(--silver); }
  .rule-left { left: 150px; }
  .rule-right { left: 551px; }

  .back-mark { left: 367px; top: 383px; }
  .back-mark .square { background: var(--silver); }
  .website {
    left: 405px; top: 386px;
    font: 700 20px "Montserrat", sans-serif; letter-spacing: 0.5px; color: var(--silver);
  }

  .production-note {
    position: absolute; left: 1008px; top: 940px;
    font: 400 16px Arial, sans-serif; color: #000;
  }
</style>
</head>
<body>
<div class="canvas">

  <section class="card card-front">
    <div class="t attorney-name">DANIEL W. HARLAN, SR.</div>
    <div class="t attorney-title">ATTORNEY AT LAW</div>

    <div class="t contact phone">P : (713) 555-0142</div>
    <div class="t contact fax">F : (832) 555-0187</div>
    <div class="t contact office-houston">4810 Katy Freeway, Suite 220<br>Houston, Texas 77055</div>

    <div class="t contact email">Daniel@harlantxlaw.com</div>
    <div class="t contact office-marathon">P.O. Box 518<br>Marathon, Texas 79617</div>

    <div class="brand-mark front-mark">
      <span class="square"></span>
      <span class="name">HARLAN</span>
    </div>
  </section>

  <section class="card card-back">
    <div class="t firm-name">THE HARLAN LAW FIRM P.C.</div>
    <span class="rule rule-left"></span>
    <div class="t firm-tagline">ATTORNEYS AT LAW</div>
    <span class="rule rule-right"></span>

    <div class="brand-mark back-mark">
      <span class="square"></span>
    </div>
    <div class="t website">HARLANTXLAW.COM</div>
  </section>

  <div class="production-note">Silver Foil stamping</div>
</div>
</body>
</html>
```